Maple Sprouts Childcare requires Double sided A6 Flyer

Design a double sided A6 flyer (105mm x 148mm) flyer for a childcare centre to promote more business. The copy for the flyer is attached so please use this copy is in the flyer so we can see what the final design would look like.

The childcare is wanting more children aged 0-5 years to come to their daycare so it needs to appeal to parents of young children and get them to come an see the centre.

The colours and fonts used should align with the style guide and logo. The client is ok to use Maple sprouts as icons if you wish but must look professional and link with the brand.

You can also look at their website for further insights - maplesproutschildcare.example.au

Target Market(s)

Parents of children aged 0-5 years located within a 10km radius of the child care centre.

Industry/Entity Type

Childcare

Font styles to use
Other font styles liked:
• Please use the style guide for fonts.

Requirements
Must have
• Be appealing and make the audience want to read the flyer and act on it.
Nice to have
• As it is a childcare it can be playful, colourful and personable. It must still look professional and modern.

```html
<!DOCTYPE html>
<html lang="en">
<head>
<meta charset="utf-8">
<title>Maple Sprouts Childcare – A6 Flyer</title>
<link href="https://fonts.googleapis.com/css2?family=Luckiest+Guy&family=Open+Sans:wght@400;600;700;800&display=swap" rel="stylesheet">
<style>
  :root {
    --teal: #0e8d95;
    --teal-dark: #0a6f77;
    --yellow: #f7d23a;
    --orange: #f08a1c;
    --green: #8cc63e;
    --green-dark: #4d8a1f;
    --cream: #fffbe9;
    --ink: #333a3d;
    --page: #eceeef;
  }
  * { box-sizing: border-box; margin: 0; padding: 0; }
  html, body { width: 872px; height: 1200px; overflow: hidden; }
  body { background: var(--page); font-family: "Open Sans", sans-serif; color: var(--ink); position: relative; }

  .display { font-family: "Luckiest Guy", "Arial Black", sans-serif; text-transform: uppercase; letter-spacing: 1px; }

  .side { position: absolute; left: 24px; width: 824px; overflow: hidden; background: #fff; box-shadow: 0 2px 6px rgba(0,0,0,.18); }
  .front { top: 18px; height: 560px; }
  .back { top: 598px; height: 584px; }

  /* FRONT */
  .front-photo { position: absolute; left: 0; top: 0; width: 450px; height: 380px;
    background: linear-gradient(160deg, #b9d98a 0%, #e9dcc2 45%, #f3c9a8 70%, #9cc65a 100%); }
  .front-bg { position: absolute; left: 450px; top: 0; width: 374px; height: 380px; background: var(--cream); }
  .tagline { position: absolute; left: 26px; top: 22px; font-size: 28px; line-height: 1.1;
    color: var(--green); -webkit-text-stroke: 1px var(--green-dark); }
  .swoosh { position: absolute; left: 0; top: 0; width: 824px; height: 560px; }
  .brand { position: absolute; left: 470px; top: 80px; width: 354px; display: flex; align-items: center; justify-content: center; gap: 10px; }
  .brand-dot { width: 34px; height: 34px; border-radius: 50%; background: var(--green); flex: none; }
  .brand-name { font-size: 28px; color: var(--teal); white-space: nowrap; }
  .slogan { position: absolute; left: 450px; top: 200px; width: 374px; text-align: center; white-space: nowrap;
    font-size: 26px; color: var(--orange); }
  .specialty { position: absolute; left: 0; top: 430px; width: 824px; text-align: center;
    font-size: 30px; line-height: 1.25; color: var(--yellow); }

  /* BACK */
  .back-top { position: absolute; left: 0; top: 0; width: 824px; height: 16px; background: var(--teal); }
  .intro-col { position: absolute; left: 30px; top: 42px; width: 380px; }
  .intro { font-size: 11.5px; line-height: 1.5; text-align: justify; }
  .tour-row { display: flex; gap: 12px; margin-top: 16px; align-items: center; }
  .tour-photo { width: 150px; height: 150px; flex: none; background: linear-gradient(150deg, #d9c7a6, #c94b3c 55%, #8fb86a); }
  .tour-call { font-weight: 800; font-size: 15.5px; line-height: 1.4; text-align: center; white-space: nowrap; }
  .places { margin-top: 18px; text-align: center; font-weight: 800; font-size: 15px; line-height: 1.4; color: var(--orange); }
  .benefits { position: absolute; left: 432px; top: 34px; width: 366px; height: 462px; background: var(--cream); border-left: 4px solid var(--teal); padding: 18px 18px 0 20px; }
  .benefits h2 { font-size: 19px; font-weight: 800; color: var(--teal); line-height: 1.25; margin-bottom: 12px; }
  .benefits ul { list-style: none; }
  .benefits li { position: relative; padding-left: 22px; font-size: 12.5px; line-height: 1.4; margin-bottom: 7px; }
  .benefits li::before { content: ""; position: absolute; left: 0; top: 4px; width: 12px; height: 12px; background: var(--green); border-radius: 2px; }
  .hours { position: absolute; left: 0; bottom: 0; width: 824px; height: 62px; background: var(--teal); display: flex; align-items: center; justify-content: center;
    font-size: 26px; color: var(--yellow); }
</style>
</head>
<body>

<section class="side front">
  <div class="front-photo" role="img" aria-label="Photo of a smiling mother reading with two young children outdoors"></div>
  <div class="front-bg"></div>
  <svg class="swoosh" viewBox="0 0 824 560" aria-hidden="true">
    <path d="M0 340 C220 390 440 320 824 290 L824 560 L0 560 Z" fill="var(--yellow)"/>
    <path d="M0 362 C230 410 450 342 824 318 L824 560 L0 560 Z" fill="var(--orange)"/>
    <path d="M0 384 C240 428 460 364 824 344 L824 560 L0 560 Z" fill="#fff"/>
    <path d="M0 396 C250 440 470 378 824 360 L824 560 L0 560 Z" fill="var(--teal)"/>
  </svg>
  <div class="tagline display">Curiosity<br>starts<br>here...</div>
  <div class="brand"><span class="brand-dot"></span><span class="brand-name display">Maple Sprouts</span></div>
  <div class="slogan display">A great place to grow</div>
  <div class="specialty display">Specialising in long<br>day care and out of school care</div>
</section>

<section class="side back">
  <div class="back-top"></div>
  <div class="intro-col">
    <p class="intro">Every parent wants the best for their child, and it's not always an easy task. That's why here at Maple Sprouts Childcare we recognise that small things matter the most and offer a welcoming environment for your child to grow developmentally through play and socialisation. Best of all, our staff are highly trained in early childhood, so rest assured you know they're in safe hands.</p>
    <div class="tour-row">
      <div class="tour-photo" role="img" aria-label="Photo of the centre's outdoor play area"></div>
      <p class="tour-call">So why not take a tour today,<br>Call us on 0400 555 012<br>and let the fun begin</p>
    </div>
    <p class="places">Places are limited so come and find us at<br>12 Harbour Terrace (Entrance Via<br>Reef Street)</p>
  </div>
  <div class="benefits">
    <h2>Take a look at some of the benefits of our center:</h2>
    <ul>
      <li>Qualified staff who nurture your child's development</li>
      <li>Kids never get bored with our massive outdoor play area</li>
      <li>Peer interaction to teach sharing, problem solving, and develop friendships</li>
      <li>Structure and routine with a well-run program by qualified staff</li>
      <li>Stability and reliability so your never left without a minder</li>
      <li>Focus on School Readiness – less separation anxiety, accustomed to classroom routines and academic readiness</li>
      <li>Child Care Rebate approved</li>
      <li>Plus much more...</li>
    </ul>
  </div>
  <div class="hours display">Opening time 6:30am – 6:00pm</div>
</section>

</body>
</html>
```